Client Fulfillment Flyer

This is a document used for internal purposes ie it is not distributed to clients. We would like it to have some colour, images etc. We are in the financial services industry, Ballarat, Victoria, Australia. www.tarrowfield.com.au and www.tarrowfieldagri.com.au

Target Market(s)

Internal training document

Industry/Entity Type

Finance And Accounting

Colors
3176b5

```html
<!DOCTYPE html>
<html lang="en">
<head>
<meta charset="utf-8">
<title>Tarrowfield &amp; Co – Client Fulfillment Flyer</title>
<link href="https://fonts.googleapis.com/css2?family=Lato:wght@400;700;900&family=Oswald:wght@600;700&display=swap" rel="stylesheet">
<style>
  :root {
    --brand-blue: #0a5ea8;
    --brand-blue-deep: #0b4f8f;
    --sky: #cfe5f8;
    --sky-soft: #e4f0fb;
    --ink: #3a3a3a;
    --paper: #ffffff;
    --backdrop: #e8ecef;
  }
  * { margin: 0; padding: 0; box-sizing: border-box; }
  html, body { width: 1200px; height: 1200px; overflow: hidden; }
  body { background: var(--backdrop); font-family: "Lato", sans-serif; position: relative; }

  .flyer {
    position: absolute; left: 204px; top: 44px;
    width: 792px; height: 1111px;
    background: var(--paper); overflow: hidden;
    box-shadow: 0 6px 24px rgba(0,0,0,.18);
  }
  .flyer-shapes { position: absolute; inset: 0; }

  .abs { position: absolute; }

  .brand { left: 22px; top: 24px; display: flex; align-items: center; gap: 14px; }
  .brand-dot { width: 78px; height: 78px; border-radius: 50%; background: var(--brand-blue); }
  .brand-name { font-family: "Lato", sans-serif; font-weight: 700; font-size: 25px; color: var(--brand-blue); letter-spacing: 1.5px; }

  .intro-title {
    left: 25px; top: 272px;
    font-family: "Oswald", sans-serif; font-weight: 700; color: #fff;
    font-size: 31px; line-height: 39px; letter-spacing: .3px;
  }
  .intro-copy {
    left: 25px; top: 406px; width: 370px;
    color: #fff; font-size: 13.2px; line-height: 20.7px;
  }
  .process-title {
    left: 25px; top: 584px;
    font-family: "Oswald", sans-serif; font-weight: 700; font-size: 18.5px; color: #fff;
  }
  .process-lead { left: 24px; top: 613px; font-size: 11.5px; font-weight: 900; color: #fff; }
  .process-list { left: 24px; top: 637px; list-style: none; color: #fff; font-size: 11px; }
  .process-list li { height: 23.3px; }
  .process-list li::before { content: "\25CF"; font-size: 8px; margin-right: 5px; vertical-align: 1px; }

  .section-heading {
    font-family: "Oswald", sans-serif; font-weight: 700; color: var(--brand-blue);
    font-size: 21px; letter-spacing: .3px; transform: translateX(-50%);
  }
  .contact-title { left: 536px; top: 763px; }
  .vision-title { left: 442px; top: 939px; }

  .contact-item {
    transform: translateX(-50%); text-align: center;
    color: var(--ink); font-weight: 700; font-size: 13.5px; line-height: 16px; white-space: nowrap;
  }
  .contact-social { left: 372px; top: 871px; }
  .contact-phone { left: 532px; top: 872px; }
  .contact-mail { left: 686px; top: 870px; }

  .vision-copy { left: 113px; top: 985px; width: 665px; color: var(--ink); font-size: 8.6px; font-weight: 700; line-height: 13px; }
  .vision-copy p { margin-bottom: 8px; }

  .site-url { left: 478px; top: 1089px; width: 237px; text-align: center; font-size: 11.5px; font-weight: 900; color: var(--brand-blue); }
</style>
</head>
<body>
<main class="flyer">
  <svg class="flyer-shapes" width="792" height="1111" viewBox="0 0 792 1111" aria-hidden="false">
    <defs>
      <linearGradient id="heroTone" x1="0" y1="0" x2="1" y2="1">
        <stop offset="0" stop-color="#e8d3c4"/>
        <stop offset=".45" stop-color="#f3ece6"/>
        <stop offset="1" stop-color="#b9c8d6"/>
      </linearGradient>
      <linearGradient id="portraitTone" x1="0" y1="0" x2="0" y2="1">
        <stop offset="0" stop-color="#f1ece7"/>
        <stop offset="1" stop-color="#cfdfec"/>
      </linearGradient>
    </defs>

    <!-- hero photo area -->
    <polygon role="img" aria-label="Photo of a smiling young man in glasses and a white t-shirt seated outdoors"
      points="470,0 792,0 792,468 160,838 0,838 0,300" fill="url(#heroTone)"/>
    <!-- light stripe along top edge of photo -->
    <polygon points="440,0 470,0 170,195 150,180" fill="var(--sky)"/>
    <!-- light stripes below photo -->
    <polygon points="792,468 792,500 110,930 100,880 160,838" fill="var(--sky)"/>
    <polygon points="792,500 792,520 120,945 110,930" fill="var(--sky-soft)"/>
    <polygon points="100,836 250,836 100,935" fill="#dfe4ea"/>
    <polygon points="420,900 460,900 100,1120 100,1090" fill="var(--sky)"/>

    <!-- main blue hexagon -->
    <polygon points="0,250 112,178 148,178 400,366 414,392 414,632 400,660 150,832 112,832 0,770"
      fill="var(--brand-blue)" stroke="var(--brand-blue)" stroke-width="12" stroke-linejoin="round"/>

    <!-- portrait hexagon frame -->
    <polygon points="0,775 100,840 100,1005 0,1068" fill="var(--brand-blue)"/>
    <polygon role="img" aria-label="Photo of a young man in glasses giving a thumbs up"
      points="0,832 82,872 82,978 0,1016" fill="url(#portraitTone)"/>

    <!-- contact icons -->
    <g fill="none" stroke="var(--brand-blue-deep)" stroke-width="2.5" stroke-linejoin="round">
      <polygon points="372,808 397,822 397,851 372,865 347,851 347,822"/>
      <polygon points="527,808 552,822 552,851 527,865 502,851 502,822"/>
      <polygon points="681,808 706,822 706,851 681,865 656,851 656,822"/>
    </g>
    <!-- social: plain square -->
    <rect x="362" y="827" width="20" height="20" rx="3" fill="var(--brand-blue-deep)"/>
    <!-- phone handset -->
    <path d="M524,827 q-5,10 0,20 l4,-2 q-3,-8 0,-16 z" fill="var(--brand-blue-deep)"/>
    <!-- envelope -->
    <rect x="671" y="829" width="20" height="14" rx="1.5" fill="var(--brand-blue-deep)"/>
    <polyline points="672,830 681,838 690,830" fill="none" stroke="#fff" stroke-width="1.6"/>

    <!-- footer band -->
    <rect x="0" y="1082" width="792" height="29" fill="var(--brand-blue)"/>
    <polygon points="500,1082 715,1082 693,1111 478,1111" fill="#fff"/>
  </svg>

  <div class="abs brand">
    <span class="brand-dot"></span>
    <span class="brand-name">TARROWFIELD &amp; CO</span>
  </div>

  <h1 class="abs intro-title">Hellow<br>We are<br>TARROWFIELD AND CO.</h1>
  <p class="abs intro-copy">We are primarily a service based business however the product we sell is Client Fulfillment.&nbsp; Client Fulfillment in simple terms means providing the services to satisfy client requirements and expectations.&nbsp; Our aim is to not only satisfy but exceed client requirements and expectations. The Client Fulfillment system is the methodology through which we deliver the result we have promised to deliver.</p>

  <h2 class="abs process-title">The Client Fulfillment Process</h2>
  <p class="abs process-lead">The areas we focus on to deliver Client Fulfillment are:</p>
  <ul class="abs process-list">
    <li>Understanding Core Purpose, Core Values, Vision and Why</li>
    <li>Client Management and Communication</li>
    <li>The Basics</li>
    <li>The Are You Financially Secure Process</li>
    <li>The Right People Doing the Right Work</li>
  </ul>

  <h2 class="abs section-heading contact-title">CONTRACT US</h2>
  <p class="abs contact-item contact-social">www.socialpage.com/<br>tarrowfieldagrisolutions</p>
  <p class="abs contact-item contact-phone">1300 555 019</p>
  <p class="abs contact-item contact-mail">info@tarrowfieldagri.com.au</p>

  <h2 class="abs section-heading vision-title">OUR VISION</h2>
  <div class="abs vision-copy">
    <p>This is our Vision across the entire Tarrowfield &amp; Co business:&nbsp; To provide all businesses and individuals with the opportunity to achieve financial security.</p>
    <p>Our business is designed so people can access all the services required to achieve financial security. We are a motivated team that embraces change and technology along with having the knowledge, skills and expertise to help committed clients achieve financial security.</p>
    <p>We believe everyone deserves this opportunity and we are committed to proactively engage with existing and future clients to share and demonstrate the positive impact we can make to their lives.&nbsp; We do not limit the number of people we can help and distance is not a barrier. Our goal by 30th June</p>
  </div>

  <p class="abs site-url">https://www.tarrowfield.com.au/</p>
</main>
</body>
</html>
```